Financial Services Company power point theme design

We need a PowerPoint theme designed for client presentations and company orientations. We do like modern designs using blue colors. attached is our logos the logo colors may change as needed to fit the theme. Landscape 16: 9 is acceptable

Industry/Entity Type

Financial Service

Colors

Designer to choose colors to be used in the design.

```html
<!DOCTYPE html>
<html lang="en">
<head>
<meta charset="utf-8">
<title>Northbridge Capital — Presentation Theme</title>
<link href="https://fonts.googleapis.com/css2?family=Roboto+Condensed:wght@400;700&family=Roboto:wght@400;700&display=swap" rel="stylesheet">
<style>
:root{
  --navy:#1b3766;
  --navy-photo:#3a5582;
  --blue:#1591d6;
  --grey:#8b9099;
  --light-grey:#c9ccd2;
  --canvas:#dcdde0;
  --ink:#3d4450;
  --white:#ffffff;
}
*{margin:0;padding:0;box-sizing:border-box}
html,body{width:1200px;height:900px;overflow:hidden;background:var(--canvas);font-family:"Roboto",sans-serif;color:var(--ink)}
.deck{position:relative;width:1200px;height:900px}
.slide{position:absolute;width:237px;height:133px;background:var(--white);overflow:hidden}
.slide > *{position:absolute}
.c1{left:194px}.c2{left:434px}.c3{left:674px}
.r1{top:44px}.r2{top:182px}.r3{top:320px}.r4{top:454px}.r5{top:590px}.r6{top:727px}
.title{left:11px;top:10px;font-family:"Roboto Condensed",sans-serif;font-size:6.5px;color:var(--navy);letter-spacing:-.1px}
.title::after{content:"";display:block;width:12px;height:.8px;background:var(--blue);margin-top:2px}
.title.light{color:var(--white)}
.brand{right:8px;top:6px;display:flex;align-items:center;gap:2px;font-family:"Roboto Condensed",sans-serif;font-weight:700;font-size:3.6px;color:var(--navy)}
.brand i{width:5px;height:5px;border-radius:50%;background:var(--navy);display:block}
.foot{left:0;bottom:0;width:100%;height:3px;background:var(--navy);color:var(--white);font-size:2px;line-height:3px;padding:0 4px;display:flex;justify-content:space-between}
.photo{background:linear-gradient(135deg,#6e86ab,#2f4a78)}
.photo.light{background:linear-gradient(135deg,#c7d3e3,#7d93b5)}
.photo.dark{background:linear-gradient(135deg,#1e3a66,#4d79b1)}
.txt{font-size:2.6px;line-height:3.3px;color:var(--ink);text-align:justify}
.txt.w{color:var(--white)}
.txt.c{text-align:center}
.bold{font-weight:700}
.ico{border-radius:50%;display:flex;align-items:center;justify-content:center}
</style>
</head>
<body>
<main class="deck">

<!-- Welcome -->
<section class="slide c1 r1">
  <div style="left:16px;top:8px;display:flex;align-items:center;gap:3px;font-family:'Roboto Condensed',sans-serif;font-weight:700;font-size:4.5px;color:var(--navy)"><i style="width:8px;height:8px;border-radius:50%;background:var(--navy);display:block"></i>NORTHBRIDGE CAPITAL</div>
  <div class="photo light" role="img" aria-label="Hands holding a tablet showing financial charts" style="left:0;top:53px;width:150px;height:60px"></div>
  <div style="left:100px;top:53px;width:137px;height:60px;background:linear-gradient(90deg,rgba(27,55,102,0),var(--navy) 45%)"></div>
  <div style="right:10px;top:65px;text-align:right;color:var(--white);font-family:'Roboto Condensed',sans-serif">
    <div style="font-size:10px;font-weight:700">WELCOME</div>
    <div style="font-size:6px;letter-spacing:1px">TO OUR PRESENTATION</div>
    <div style="font-size:2.8px;font-weight:700;margin-top:3px">Lakeview, March 25, 2016</div>
  </div>
  <div class="txt" style="left:17px;top:120px;font-size:2px;color:var(--navy)">© 2016 All rights reserved. Content and brand elements are the property of the company.</div>
  <div style="left:0;bottom:0;width:100%;height:3px;background:var(--navy)"></div>
</section>

<!-- Contents -->
<section class="slide c2 r1" style="background:var(--navy-photo)">
  <div class="photo" role="img" aria-label="Desk with tablet and hands in muted blue" style="left:0;top:0;width:100%;height:100%;opacity:.6"></div>
  <div style="left:37px;top:34px;color:var(--white);font-family:'Roboto Condensed',sans-serif">
    <div style="font-size:3px">TABLE OF</div>
    <div style="font-size:8px">CONTENTS</div>
  </div>
  <div style="left:50px;top:72px;width:150px;display:grid;grid-template-columns:1fr 1fr;row-gap:9px;column-gap:10px;color:var(--white);font-size:2.4px;font-weight:700;line-height:3px">
    <div style="display:flex;gap:4px"><b class="ico" style="width:8px;height:8px;background:var(--blue);font-size:3px">1</b><span>LOREM IPSUM COLOR SIT<br>MET COLOR SIT MET</span></div>
    <div style="display:flex;gap:4px"><b class="ico" style="width:8px;height:8px;background:var(--blue);font-size:3px">4</b><span>LOREM IPSUM COLOR SIT<br>MET COLOR SIT MET</span></div>
    <div style="display:flex;gap:4px"><b class="ico" style="width:8px;height:8px;background:var(--blue);font-size:3px">2</b><span>LOREM IPSUM COLOR SIT<br>MET COLOR SIT MET</span></div>
    <div style="display:flex;gap:4px"><b class="ico" style="width:8px;height:8px;background:var(--blue);font-size:3px">5</b><span>LOREM IPSUM COLOR SIT<br>MET COLOR SIT MET</span></div>
    <div style="display:flex;gap:4px"><b class="ico" style="width:8px;height:8px;background:var(--blue);font-size:3px">3</b><span>LOREM IPSUM COLOR SIT<br>MET COLOR SIT MET</span></div>
    <div style="display:flex;gap:4px"><b class="ico" style="width:8px;height:8px;background:var(--blue);font-size:3px">6</b><span>LOREM IPSUM COLOR SIT<br>MET COLOR SIT MET</span></div>
  </div>
</section>

<!-- Vision & Mission -->
<section class="slide c3 r1" style="background:var(--blue)">
  <div class="photo" role="img" aria-label="Business meeting table with papers and coffee" style="left:0;top:0;width:100%;height:72px"></div>
  <div class="title light" style="top:11px;font-size:5.5px">VISION &amp; MISSION</div>
  <svg style="left:52px;top:57px" width="22" height="22" viewBox="0 0 22 22"><circle cx="11" cy="11" r="10" fill="var(--navy)" stroke="#fff" stroke-width="1.2"/><circle cx="8.5" cy="11.5" r="2.5" fill="none" stroke="#fff" stroke-width="1.2"/><circle cx="13.5" cy="11.5" r="2.5" fill="none" stroke="#fff" stroke-width="1.2"/></svg>
  <svg style="left:151px;top:57px" width="22" height="22" viewBox="0 0 22 22"><circle cx="11" cy="11" r="10" fill="var(--navy)" stroke="#fff" stroke-width="1.2"/><path d="M6 14a5 5 0 1 1 10 0" fill="none" stroke="#fff" stroke-width="1.2"/><path d="M11 14l2.5-3" stroke="#fff" stroke-width="1.2"/></svg>
  <div class="txt w c" style="left:30px;top:89px;width:70px;font-size:2.8px">To provide state of the art logistics and supply chain solutions to the defined needs of our customers using the best people, processes and systems in creating efficient and effective results.</div>
  <div class="txt w c" style="left:127px;top:89px;width:70px;font-size:2.8px">To provide state of the art logistics and supply chain solutions to the defined needs of our customers using the best people, processes and systems in creating efficient and effective results.</div>
</section>

<!-- About 1 -->
<section class="slide c1 r2">
  <h2 class="title">ABOUT US</h2>
  <div class="brand"><i></i>NORTHBRIDGE</div>
  <div style="left:0;top:45px;width:78px;height:43px;background:var(--blue);padding:13px 6px 0 14px;color:var(--white);font-size:2.4px;font-weight:700;line-height:3.2px">LOREM IPSUM COLOR SIT MET CONSECTUR ADIPISCING ELIT SED DO EIUSMOD TEMPOR INCIDIDUNT UT LABORE ET DOLORE MAGNA</div>
  <div class="photo light" role="img" aria-label="Team of business people smiling" style="left:78px;top:45px;width:159px;height:43px"></div>
  <div class="txt" style="left:77px;top:95px;width:148px">Lorem ipsum dolor sit amet, consectetur adipiscing elit, sed do eiusmod tempor incididunt ut labore et dolore magna aliqua. Ut enim ad minim veniam, quis nostrud exercitation ullamco laboris nisi ut aliquip ex ea commodo consequat. Duis aute irure dolor in reprehenderit in voluptate velit esse cillum dolore eu fugiat nulla pariatur.</div>
  <footer class="foot"><span>© 2016 All rights reserved</span><span>02</span></footer>
</section>

<!-- About 2 -->
<section class="slide c2 r2">
  <h2 class="title">ABOUT US</h2>
  <div class="brand"><i></i>NORTHBRIDGE</div>
  <div style="left:21px;top:30px;width:51px;height:16px;background:var(--blue);color:#fff;font-size:2.3px;font-weight:700;padding:6px 0 0 8px">LOREM IPSUM COLOR</div>
  <div class="photo light" role="img" aria-label="Businessman pointing at a chart" style="left:72px;top:30px;width:48px;height:27px"></div>
  <div class="txt w bold" style="left:120px;top:30px;width:94px;height:27px;background:var(--navy);padding:4px 5px">Lorem ipsum dolor sit amet, consectetur adipiscing elit, sed do eiusmod tempor incididunt ut labore et dolore magna aliqua.</div>
  <div class="txt w bold" style="left:21px;top:57px;width:99px;height:29px;background:var(--navy);padding:7px 5px">Lorem ipsum dolor sit amet, consectetur adipiscing elit, sed do eiusmod tempor incididunt ut labore et dolore magna aliqua.</div>
  <div style="left:120px;top:57px;width:48px;height:29px;background:var(--blue);color:#fff;font-size:2.3px;font-weight:700;padding:13px 0 0 8px">LOREM IPSUM COLOR</div>
  <div class="photo light" role="img" aria-label="Business team around a laptop" style="left:168px;top:57px;width:46px;height:29px"></div>
  <div class="photo light" role="img" aria-label="Group of smiling colleagues" style="left:21px;top:86px;width:50px;height:30px"></div>
  <div style="left:71px;top:86px;width:49px;height:30px;background:var(--navy);color:#fff;font-size:2.3px;font-weight:700;padding:13px 0 0 6px">LOREM IPSUM COLOR</div>
  <div class="txt w bold" style="left:120px;top:86px;width:94px;height:30px;background:var(--navy);padding:5px 5px">Lorem ipsum dolor sit amet, consectetur adipiscing elit, sed do eiusmod tempor incididunt ut labore et dolore magna aliqua.</div>
  <footer class="foot"><span>© 2016 All rights reserved</span><span>03</span></footer>
</section>

<!-- About 3 -->
<section class="slide c3 r2">
  <h2 class="title">ABOUT US</h2>
  <div class="brand"><i></i>NORTHBRIDGE</div>
  <div class="photo light" role="img" aria-label="Business people shaking hands" style="left:10px;top:36px;width:51px;height:32px"></div>
  <div class="txt c" style="left:10px;top:71px;width:51px;color:var(--blue)">Lorem ipsum dolor sit amet, consectetur adipiscing elit sed do eiusmod</div>
  <div class="txt" style="left:70px;top:34px;width:74px">Lorem ipsum dolor sit amet, consectetur adipiscing elit, sed do eiusmod tempor incididunt ut labore et dolore magna aliqua. Ut enim ad minim veniam, quis nostrud exercitation ullamco laboris nisi ut aliquip ex ea commodo consequat. Duis aute irure dolor in reprehenderit in voluptate velit esse cillum dolore eu fugiat nulla pariatur.</div>
  <div class="txt" style="left:152px;top:34px;width:74px">Lorem ipsum dolor sit amet, consectetur adipiscing elit, sed do eiusmod tempor incididunt ut labore et dolore magna aliqua. Ut enim ad minim veniam, quis nostrud exercitation ullamco laboris nisi ut aliquip ex ea commodo consequat. Duis aute irure dolor in reprehenderit in voluptate velit esse cillum dolore eu fugiat nulla pariatur.</div>
  <div class="txt" style="left:70px;top:82px;width:74px">Lorem ipsum dolor sit amet, consectetur adipiscing elit, sed do eiusmod tempor incididunt ut labore et dolore magna aliqua. Ut enim ad minim veniam, quis nostrud exercitation ullamco laboris nisi ut aliquip ex ea commodo.</div>
  <div class="txt" style="left:152px;top:82px;width:74px">Lorem ipsum dolor sit amet, consectetur adipiscing elit, sed do eiusmod tempor incididunt ut labore et dolore magna aliqua. Ut enim ad minim veniam, quis nostrud exercitation ullamco laboris nisi ut aliquip ex ea commodo.</div>
  <footer class="foot"><span>© 2016 All rights reserved</span><span>04</span></footer>
</section>

<!-- About 4 -->
<section class="slide c1 r3">
  <h2 class="title">ABOUT US</h2>
  <div class="brand"><i></i>NORTHBRIDGE</div>
  <div style="left:12px;top:43px;font-size:4.2px;font-weight:700;color:var(--navy)">Lorem ipsum dolor sit amet</div>
  <div class="txt" style="left:12px;top:50px;width:86px">Lorem ipsum dolor sit amet, consectetur adipiscing elit, sed do eiusmod tempor incididunt ut labore et dolore magna aliqua. Ut enim ad minim veniam, quis nostrud exercitation ullamco laboris nisi ut aliquip ex ea commodo consequat. Duis aute irure dolor in reprehenderit in voluptate velit esse cillum dolore eu fugiat nulla pariatur.</div>
  <div class="txt" style="left:12px;top:95px;width:86px">Lorem ipsum dolor sit amet, consectetur adipiscing elit, sed do eiusmod tempor incididunt ut labore et dolore magna aliqua. Ut enim ad minim veniam, quis.</div>
  <div class="photo dark" role="img" aria-label="Hand touching digital interface" style="left:103px;top:41px;width:34px;height:40px"></div>
  <div class="photo dark" role="img" aria-label="Finger on glowing screen" style="left:146px;top:41px;width:34px;height:40px"></div>
  <div class="photo dark" role="img" aria-label="Hands holding a glowing globe" style="left:188px;top:41px;width:34px;height:40px"></div>
  <div class="txt" style="left:103px;top:84px;width:34px">Duis aute irure dolor in reprehenderit in voluptate velit esse cillum dolore eu fugiat nulla pariatur.</div>
  <div class="txt" style="left:146px;top:84px;width:34px">Duis aute irure dolor in reprehenderit in voluptate velit esse cillum dolore eu fugiat nulla pariatur.</div>
  <div class="txt" style="left:188px;top:84px;width:34px">Duis aute irure dolor in reprehenderit in voluptate velit esse cillum dolore eu fugiat nulla pariatur.</div>
  <footer class="foot"><span>© 2016 All rights reserved</span><span>05</span></footer>
</section>

<!-- About 5 -->
<section class="slide c2 r3">
  <h2 class="title">ABOUT US</h2>
  <div class="brand"><i></i>NORTHBRIDGE</div>
  <div class="photo dark" role="img" aria-label="Hands with glowing globe" style="left:25px;top:36px;width:57px;height:39px"></div>
  <div class="photo light" role="img" aria-label="Business team meeting" style="left:87px;top:36px;width:57px;height:39px"></div>
  <div class="photo dark" role="img" aria-label="Hand touching network graphic" style="left:149px;top:36px;width:57px;height:39px"></div>
  <div class="txt bold" style="left:25px;top:79px;color:var(--navy)">Lorem ipsum dolor sit amet</div>
  <div class="txt bold" style="left:87px;top:79px;color:var(--navy)">Lorem ipsum dolor sit amet</div>
  <div class="txt bold" style="left:149px;top:79px;color:var(--navy)">Lorem ipsum dolor sit amet</div>
  <div class="txt" style="left:25px;top:85px;width:57px">Ut enim ad minim veniam, quis nostrud exercitation ullamco laboris nisi ut aliquip ex ea commodo consequat. Duis aute irure dolor in reprehenderit velit esse cillum dolore eu fugiat.</div>
  <div class="txt" style="left:87px;top:85px;width:57px">Ut enim ad minim veniam, quis nostrud exercitation ullamco laboris nisi ut aliquip ex ea commodo consequat. Duis aute irure dolor in reprehenderit velit esse cillum dolore eu fugiat.</div>
  <div class="txt" style="left:149px;top:85px;width:57px">Ut enim ad minim veniam, quis nostrud exercitation ullamco laboris nisi ut aliquip ex ea commodo consequat. Duis aute irure dolor in reprehenderit velit esse cillum dolore eu fugiat.</div>
  <footer class="foot"><span>© 2016 All rights reserved</span><span>06</span></footer>
</section>

<!-- Our team -->
<section class="slide c3 r3">
  <h2 class="title">OUR TEAM</h2>
  <div class="brand"><i></i>NORTHBRIDGE</div>
  <div class="photo light" role="img" aria-label="Portrait of team member" style="left:34px;top:35px;width:28px;height:28px;border-radius:50%;border:1px solid var(--navy)"></div>
  <div class="photo light" role="img" aria-label="Portrait of team member" style="left:104px;top:35px;width:28px;height:28px;border-radius:50%;border:1px solid var(--navy)"></div>
  <div class="photo light" role="img" aria-label="Portrait of team member" style="left:174px;top:35px;width:28px;height:28px;border-radius:50%;border:1px solid var(--navy)"></div>
  <div class="txt c" style="left:23px;top:66px;width:50px"><b style="color:var(--navy)">JONATHAN DOE</b><br>President<br><br>Dolor sit amet, consectetur adipiscing elit, sed do eiusmod tempor incididunt ut labore et dolore magna aliqua. Ut enim ad minim veniam, quis nostrud exercitation.</div>
  <div class="txt c" style="left:93px;top:66px;width:50px"><b style="color:var(--navy)">MELANIE DOE</b><br>CEO / Founder<br><br>Dolor sit amet, consectetur adipiscing elit, sed do eiusmod tempor incididunt ut labore et dolore magna aliqua. Ut enim ad minim veniam, quis nostrud exercitation.</div>
  <div class="txt c" style="left:163px;top:66px;width:50px"><b style="color:var(--navy)">NATALIE DOE</b><br>Vice President<br><br>Dolor sit amet, consectetur adipiscing elit, sed do eiusmod tempor incididunt ut labore et dolore magna aliqua. Ut enim ad minim veniam, quis nostrud exercitation.</div>
  <footer class="foot"><span>© 2016 All rights reserved</span><span>07</span></footer>
</section>

<!-- Cycle -->
<section class="slide c1 r4">
  <h2 class="title">ABOUT US</h2>
  <div class="brand"><i></i>NORTHBRIDGE</div>
  <svg style="left:82px;top:32px" width="78" height="78" viewBox="0 0 78 78">
    <circle cx="39" cy="39" r="30" fill="none" stroke="var(--navy)" stroke-width="15" stroke-dasharray="47 141.5" transform="rotate(-90 39 39)"/>
    <circle cx="39" cy="39" r="30" fill="none" stroke="var(--grey)" stroke-width="15" stroke-dasharray="47 141.5" transform="rotate(0 39 39)"/>
    <circle cx="39" cy="39" r="30" fill="none" stroke="var(--blue)" stroke-width="15" stroke-dasharray="47 141.5" transform="rotate(90 39 39)"/>
    <circle cx="39" cy="39" r="30" fill="none" stroke="var(--grey)" stroke-width="15" stroke-dasharray="47 141.5" transform="rotate(180 39 39)"/>
    <circle cx="57" cy="12" r="8" fill="#fff" stroke="var(--navy)" stroke-width="1.5"/><path d="M53 13l8-4-3 8-1-3z" fill="var(--navy)"/>
    <circle cx="66" cy="57" r="8" fill="#fff" stroke="var(--grey)" stroke-width="1.5"/><circle cx="66" cy="57" r="3" fill="none" stroke="var(--grey)"/>
    <circle cx="39" cy="70" r="8" fill="#fff" stroke="var(--blue)" stroke-width="1.5"/><path d="M39 74c-3-4-3-5-3-6a3 3 0 0 1 6 0c0 1 0 2-3 6z" fill="var(--blue)"/>
    <circle cx="12" cy="39" r="8" fill="#fff" stroke="var(--grey)" stroke-width="1.5"/><path d="M8 37h8l-4 5z" fill="none" stroke="var(--grey)"/>
  </svg>
  <div style="left:26px;top:59px;font-size:3.5px;font-weight:700;color:var(--navy)">➤ Lorem Ipsum</div>
  <div class="txt c" style="left:28px;top:64px;width:44px">Dolor sit amet, consectetur adipiscing elit, sed do eiusmod tempor</div>
  <div style="left:26px;top:97px;font-size:3.5px;color:var(--grey)">◇ Lorem Ipsum</div>
  <div class="txt c" style="left:28px;top:102px;width:44px">Dolor sit amet, consectetur adipiscing elit, sed do eiusmod tempor</div>
  <div style="left:168px;top:59px;font-size:3.5px;color:var(--grey)">◎ Lorem Ipsum</div>
  <div class="txt" style="left:170px;top:64px;width:44px">Dolor sit amet, consectetur adipiscing elit, sed do eiusmod tempor</div>
  <div style="left:168px;top:97px;font-size:3.5px;color:var(--blue)">● Lorem Ipsum</div>
  <div class="txt" style="left:170px;top:102px;width:44px">Dolor sit amet, consectetur adipiscing elit, sed do eiusmod tempor</div>
  <footer class="foot"><span>© 2016 All rights reserved</span><span>08</span></footer>
</section>

<!-- Percentages donut -->
<section class="slide c2 r4">
  <h2 class="title">ABOUT US</h2>
  <div class="brand"><i></i>NORTHBRIDGE</div>
  <svg style="left:48px;top:35px" width="72" height="72" viewBox="0 0 72 72">
    <circle cx="36" cy="36" r="28" fill="none" stroke="var(--navy)" stroke-width="11" stroke-dasharray="102 176" transform="rotate(-90 36 36)"/>
    <circle cx="36" cy="36" r="28" fill="none" stroke="var(--blue)" stroke-width="11" stroke-dasharray="21 176" stroke-dashoffset="-102" transform="rotate(-90 36 36)"/>
    <circle cx="36" cy="36" r="28" fill="none" stroke="var(--grey)" stroke-width="11" stroke-dasharray="23 176" stroke-dashoffset="-123" transform="rotate(-90 36 36)"/>
    <circle cx="36" cy="36" r="28" fill="none" stroke="var(--blue)" stroke-width="11" stroke-dasharray="30 176" stroke-dashoffset="-146" transform="rotate(-90 36 36)"/>
    <circle cx="36" cy="26" r="3.5" fill="var(--navy)"/><rect x="32" y="31" width="8" height="12" rx="2" fill="var(--navy)"/><rect x="33" y="42" width="2.5" height="8" fill="var(--navy)"/><rect x="36.5" y="42" width="2.5" height="8" fill="var(--navy)"/>
  </svg>
  <div style="left:24px;top:28px;font-size:6px;font-weight:700;color:var(--blue)">17%</div>
  <div style="left:18px;top:46px;font-size:6px;color:var(--grey)">13%</div>
  <div style="left:29px;top:88px;font-size:6px;font-weight:700;color:var(--blue)">12%</div>
  <div style="left:120px;top:29px;font-size:8px;font-weight:700;color:var(--navy)">58%</div>
  <div class="txt" style="left:146px;top:52px;width:72px"><b style="color:var(--navy)">Lorem ipsum dolor sit amet</b><br>consectetur adipiscing elit, sed do eiusmod tempor incididunt ut labore et dolore magna aliqua. Ut enim ad minim veniam, quis nostrud exercitation ullamco laboris nisi ut aliquip ex ea commodo consequat. Duis aute irure dolor in reprehenderit in voluptate velit esse cillum.</div>
  <footer class="foot"><span>© 2016 All rights reserved</span><span>09</span></footer>
</section>

<!-- Icons with photo -->
<section class="slide c3 r4">
  <div class="photo" role="img" aria-label="Hand pointing at financial charts on paper" style="left:0;top:0;width:100%;height:64px"></div>
  <h2 class="title light">ABOUT US</h2>
  <div style="left:18px;top:74px;width:200px;display:grid;grid-template-columns:repeat(4,1fr);gap:5px">
    <div class="txt c"><span class="ico" style="width:12px;height:12px;border:1px solid var(--navy);margin:0 auto 4px;font-size:5px;color:var(--navy)">⌕</span>Dolor sit amet, consectetur adipiscing elit, sed do eiusmod tempor</div>
    <div class="txt c"><span class="ico" style="width:12px;height:12px;border:1px solid var(--navy);margin:0 auto 4px;font-size:5px;color:var(--navy)">▮</span>Dolor sit amet, consectetur adipiscing elit, sed do eiusmod tempor</div>
    <div class="txt c"><span class="ico" style="width:12px;height:12px;border:1px solid var(--navy);margin:0 auto 4px;font-size:5px;color:var(--navy)">◷</span>Dolor sit amet, consectetur adipiscing elit, sed do eiusmod tempor</div>
    <div class="txt c"><span class="ico" style="width:12px;height:12px;border:1px solid var(--navy);margin:0 auto 4px;font-size:5px;color:var(--navy)">◆</span>Dolor sit amet, consectetur adipiscing elit, sed do eiusmod tempor</div>
  </div>
  <footer class="foot"><span>© 2016 All rights reserved</span><span>10</span></footer>
</section>

<!-- Service boxes -->
<section class="slide c1 r5">
  <h2 class="title">ABOUT US</h2>
  <div class="brand"><i></i>NORTHBRIDGE</div>
  <div style="left:11px;top:34px;width:216px;display:grid;grid-template-columns:repeat(4,1fr);gap:4px;color:#fff">
    <div><div style="background:var(--navy);height:30px;text-align:center;font-size:2.5px;font-weight:700;padding-top:5px"><div style="font-size:8px">◆</div>MANAGEMENT<br>SOLUTIONS</div><div class="txt w c" style="background:var(--grey);height:48px;margin-top:1px;padding:4px 3px">Dolor sit amet, consectetur adipiscing elit, sed do eiusmod tempor incididunt ut labore et dolore magna aliqua.</div></div>
    <div><div style="background:var(--grey);height:30px;text-align:center;font-size:2.5px;font-weight:700;padding-top:5px"><div style="font-size:8px">ⓘ</div>INFORMATION<br>SOLUTIONS</div><div class="txt w c" style="background:var(--navy);height:48px;margin-top:1px;padding:4px 3px">Dolor sit amet, consectetur adipiscing elit, sed do eiusmod tempor incididunt ut labore et dolore magna aliqua.</div></div>
    <div><div style="background:var(--navy);height:30px;text-align:center;font-size:2.5px;font-weight:700;padding-top:5px"><div style="font-size:8px">✦</div>PROFESSIONAL<br>SERVICES</div><div class="txt w c" style="background:var(--grey);height:48px;margin-top:1px;padding:4px 3px">Dolor sit amet, consectetur adipiscing elit, sed do eiusmod tempor incididunt ut labore et dolore magna aliqua.</div></div>
    <div><div style="background:var(--grey);height:30px;text-align:center;font-size:2.5px;font-weight:700;padding-top:5px"><div style="font-size:8px">✳</div>ORGANIZATIONAL<br>TRANSFORMATION</div><div class="txt w c" style="background:var(--navy);height:48px;margin-top:1px;padding:4px 3px">Dolor sit amet, consectetur adipiscing elit, sed do eiusmod tempor incididunt ut labore et dolore magna aliqua.</div></div>
  </div>
  <footer class="foot"><span>© 2016 All rights reserved</span><span>11</span></footer>
</section>

<!-- Bar chart -->
<section class="slide c2 r5">
  <h2 class="title" style="left:15px">OUR CHART</h2>
  <div class="brand"><i></i>NORTHBRIDGE</div>
  <div class="txt" style="left:21px;top:40px;width:112px"><b>Lorem ipsum dolor sit amet</b><br>consectetur adipiscing elit, sed do eiusmod tempor incididunt ut labore et dolore magna aliqua. Ut enim ad minim veniam, quis nostrud exercitation ullamco laboris nisi ut aliquip ex ea commodo consequat. Duis aute irure dolor in reprehenderit in voluptate velit esse cillum dolore eu fugiat nulla pariatur.</div>
  <div class="txt" style="left:21px;top:76px;width:112px"><b>Lorem ipsum dolor sit amet</b><br>consectetur adipiscing elit, sed do eiusmod tempor incididunt ut labore et dolore magna aliqua. Ut enim ad minim veniam, quis nostrud exercitation ullamco laboris nisi ut aliquip ex ea commodo consequat. Duis aute irure dolor in reprehenderit in voluptate velit esse cillum dolore eu.</div>
  <svg style="left:148px;top:27px" width="72" height="44" viewBox="0 0 72 44">
    <line x1="2" y1="0" x2="2" y2="38" stroke="var(--light-grey)" stroke-width=".5"/>
    <line x1="2" y1="38" x2="72" y2="38" stroke="var(--light-grey)" stroke-width=".5"/>
    <g fill="var(--navy)"><rect x="6" y="16" width="3" height="22"/><rect x="22" y="10" width="3" height="28"/><rect x="38" y="18" width="3" height="20"/><rect x="54" y="12" width="3" height="26"/></g>
    <g fill="var(--grey)"><rect x="10" y="24" width="3" height="14"/><rect x="26" y="20" width="3" height="18"/><rect x="42" y="26" width="3" height="12"/><rect x="58" y="20" width="3" height="18"/></g>
    <g fill="var(--blue)"><rect x="14" y="22" width="3" height="16"/><rect x="30" y="26" width="3" height="12"/><rect x="46" y="14" width="3" height="24"/><rect x="62" y="6" width="3" height="32"/></g>
    <g font-size="2.2" fill="var(--ink)" font-family="Roboto,sans-serif"><text x="6" y="43">2008</text><text x="22" y="43">2009</text><text x="38" y="43">2011</text><text x="54" y="43">2013</text></g>
  </svg>
  <div class="txt" style="left:158px;top:75px;width:50px"><span style="color:var(--navy)">■</span> <b>LOREM IPSUM</b><br>Lorem ipsum dolor sit amet, consectetur adipiscing elit.<br><span style="color:var(--grey)">■</span> <b>LOREM IPSUM</b><br>Lorem ipsum dolor sit amet, consectetur adipiscing elit.<br><span style="color:var(--blue)">■</span> <b>LOREM IPSUM</b></div>
  <footer class="foot"><span>© 2016 All rights reserved</span><span>12</span></footer>
</section>

<!-- Progress rings -->
<section class="slide c3 r5">
  <h2 class="title">OUR CHART</h2>
  <div class="brand"><i></i>NORTHBRIDGE</div>
  <svg style="left:30px;top:46px" width="176" height="30" viewBox="0 0 176 30">
    <g fill="none" stroke-width="2.5">
      <circle cx="15" cy="15" r="13" stroke="var(--light-grey)"/><circle cx="15" cy="15" r="13" stroke="var(--navy)" stroke-dasharray="66 82" transform="rotate(-90 15 15)"/>
      <circle cx="88" cy="15" r="13" stroke="var(--light-grey)"/><circle cx="88" cy="15" r="13" stroke="var(--blue)" stroke-dasharray="59 82" transform="rotate(-90 88 15)"/>
      <circle cx="161" cy="15" r="13" stroke="var(--light-grey)"/><circle cx="161" cy="15" r="13" stroke="var(--blue)" stroke-dasharray="52 82" transform="rotate(-90 161 15)"/>
    </g>
    <g font-size="5.5" font-weight="700" fill="var(--navy)" font-family="Roboto,sans-serif" text-anchor="middle"><text x="15" y="17">81%</text><text x="88" y="17">72%</text><text x="161" y="17">63%</text></g>
  </svg>
  <div class="txt c" style="left:25px;top:88px;width:60px">Dolor sit amet, consectetur adipiscing elit, sed do eiusmod tempor incididunt ut labore et dolore magna aliqua. Ut enim ad minim veniam, quis nostrud.</div>
  <div class="txt c" style="left:98px;top:88px;width:60px">Dolor sit amet, consectetur adipiscing elit, sed do eiusmod tempor incididunt ut labore et dolore magna aliqua. Ut enim ad minim veniam, quis nostrud.</div>
  <div class="txt c" style="left:165px;top:88px;width:60px">Dolor sit amet, consectetur adipiscing elit, sed do eiusmod tempor incididunt ut labore et dolore magna aliqua. Ut enim ad minim veniam, quis nostrud.</div>
  <footer class="foot"><span>© 2016 All rights reserved</span><span>13</span></footer>
</section>

<!-- Image text -->
<section class="slide c1 r6">
  <div style="left:0;top:0;width:101px;height:100%;background:var(--navy)"></div>
  <h2 class="title light">IMAGE TEXT</h2>
  <div class="txt w bold" style="left:14px;top:53px;width:76px">Lorem ipsum dolor sit amet, consectetur adipiscing elit, sed do eiusmod tempor incididunt ut labore et dolore magna aliqua. Ut enim ad minim veniam, quis nostrud exercitation ullamco laboris nisi ut aliquip ex ea commodo consequat. Duis aute irure dolor in reprehenderit in voluptate velit esse cillum dolore eu fugiat nulla pariatur.</div>
  <div style="left:3px;bottom:3px;font-family:'Roboto Condensed',sans-serif;font-weight:700;font-size:3px;color:var(--navy);background:#fff;padding:1px 2px">NORTHBRIDGE</div>
  <div class="photo light" role="img" aria-label="Smiling business team in black and white" style="left:101px;top:0;width:136px;height:100%;background:linear-gradient(135deg,#eaeaea,#8d8d8d)"></div>
</section>

<!-- Section title -->
<section class="slide c2 r6" style="background:var(--navy-photo)">
  <div class="photo" role="img" aria-label="Colleagues working together in an office" style="left:0;top:0;width:100%;height:100%;opacity:.7"></div>
  <svg style="left:105px;top:48px" width="28" height="28" viewBox="0 0 28 28"><circle cx="14" cy="14" r="14" fill="#fff"/><circle cx="15" cy="7.5" r="2.2" fill="var(--blue)"/><path d="M11 12h6l-2 10h2v1.5h-6V22h1.5l1.5-8h-3z" fill="var(--blue)"/></svg>
  <div style="left:0;top:88px;width:100%;text-align:center;font-family:'Roboto Condensed',sans-serif;font-size:6px;color:#fff">SECTION TITLE</div>
</section>

<!-- Contact -->
<section class="slide c3 r6">
  <div style="left:18px;top:33px;display:flex;align-items:center;gap:3px;font-family:'Roboto Condensed',sans-serif;font-weight:700;font-size:4.5px;color:var(--navy)"><i style="width:8px;height:8px;border-radius:50%;background:var(--navy);display:block"></i>NORTHBRIDGE CAPITAL</div>
  <div role="img" aria-label="Street map of the office location" style="left:0;top:53px;width:100%;height:60px;background:linear-gradient(135deg,#eef0f2,#d6dbe2)"></div>
  <svg style="left:193px;top:81px" width="6" height="9" viewBox="0 0 6 9"><path d="M3 9C0 5 0 4 0 3a3 3 0 0 1 6 0c0 1 0 2-3 6z" fill="#d0021b"/></svg>
  <div style="left:0;top:113px;width:100%;height:20px;background:var(--navy);color:#fff;font-size:2.8px;display:flex;justify-content:space-around;align-items:center">
    <span><b style="color:var(--blue)">●</b> 1200 Harbor Lane Ste 400</span>
    <span><b style="color:var(--blue)">●</b> hello@northbridge.example</span>
    <span><b style="color:var(--blue)">●</b> www.northbridge.example</span>
  </div>
</section>

</main>
</body>
</html>
```